Brevant Business Card

I have a business that is called "Brevant Electrical Products LTD" My company deals with top of the range laptops and mobile phones that are exclusive. I need a business card that will be eye catching but not over complicated.

Target Market(s)

Adults aged 19 to 50
Upper middle class

Industry/Entity Type

Business

Requirements
Must have
• Company name/logo (file attached)
• It must have my contact information which is:

• Name: Dale Marwick

• Position: Managing Director 

• Business Address: 7 Hapton Row, London, W4 9QD

• Contact Number: 02085193604
• Mobile: 07814260537
• Email: info@brevant-goods.co.uk
Nice to have
• Simple and stylish
• Eye catching

```html
<!DOCTYPE html>
<html lang="en">
<head>
<meta charset="utf-8">
<title>Brevant Electrical Products – Business Card</title>
<link rel="stylesheet" href="https://fonts.googleapis.com/css2?family=Source+Sans+3:ital,wght@0,400;1,400&display=swap">
<style>
  :root {
    --frame: #8fa9c0;
    --ink: #7b9ab6;
    --paper: #ffffff;
    --wedge: #c9d8e6;
    --art-light: #eef3f8;
    --art-mid: #b7c9da;
  }
  * { box-sizing: border-box; margin: 0; padding: 0; }
  html, body {
    width: 1200px;
    height: 778px;
    overflow: hidden;
    background: var(--paper);
  }
  .card {
    position: relative;
    width: 1200px;
    height: 778px;
    background: var(--paper);
    border: 16px solid var(--frame);
    border-radius: 38px;
    overflow: hidden;
    font-family: "Source Sans 3", "Myriad Pro", sans-serif;
    color: var(--ink);
  }
  .identity {
    position: absolute;
    left: 36px;
    top: 56px;
    font-size: 34px;
    line-height: 1.3;
  }
  .identity .role { font-style: italic; }
  .brand-name {
    position: absolute;
    right: 62px;
    top: 84px;
    font-size: 52px;
    letter-spacing: 2px;
    color: var(--ink);
  }
  .corner-art {
    position: absolute;
    left: 0;
    top: 0;
    width: 1168px;
    height: 746px;
  }
  .contact {
    position: absolute;
    left: 36px;
    top: 488px;
    font-size: 35px;
    line-height: 49px;
  }
</style>
</head>
<body>
  <div class="card">
    <svg class="corner-art" viewBox="0 0 1168 746" aria-hidden="false">
      <defs>
        <linearGradient id="artTone" x1="0" y1="0" x2="1" y2="1">
          <stop offset="0" stop-color="var(--art-light)"/>
          <stop offset="1" stop-color="var(--art-mid)"/>
        </linearGradient>
      </defs>
      <polygon class="wedge" points="660,746 1168,570 1168,746" fill="var(--wedge)"/>
      <rect role="img" aria-label="Illustration of a laptop and a mobile phone" x="640" y="390" width="510" height="330" rx="40" fill="url(#artTone)" opacity="0.85"/>
    </svg>

    <header class="identity">
      <p class="name">Dale Marwick</p>
      <p class="role">Managing Director</p>
    </header>

    <p class="brand-name">BREVANT</p>

    <address class="contact" style="font-style: normal;">
      <p>Business Address: 7 Hapton Row,</p>
      <p>London, W4 9QD</p>
      <p>Contact Number: 02085193604</p>
      <p>Mobile: 07814260537</p>
      <p>Email: info@brevant-goods.co.uk</p>
    </address>
  </div>
</body>
</html>
```